massage therapy Business Card Design

massage therapy business card
I would like a custom logo created as well.
My vision is angel wings with the WB business initials in between them.
A very simple design.
Colors preferred are light blues and greens.

Target Market(s)

Massage, Spa, fitness

Industry/Entity Type

Massage Therapy

Contact Information for Business Card

A Willow Breeze
Mara Quint
Massage Therapist and Flowing Pulse Method Practitioner
2718 Bramblewood Lane, Lindenvale, AR 72000
501-384-6190
mara.willowbreeze@mailnest.example

Colors
abd036
33a6d7
3176b5
0255a3
0392cd
9bcb3c
cadf82

Requirements
Must have
• the logo must have angel wing.

```html
<!DOCTYPE html>
<html lang="en">
<head>
<meta charset="utf-8">
<title>A Willow Breeze – Business Card</title>
<link href="https://fonts.googleapis.com/css2?family=Montserrat:wght@600;700;800&display=swap" rel="stylesheet">
<style>
  :root {
    --backdrop: #161d20;
    --card-white: #ffffff;
    --leaf-green: #9bc424;
    --band-green: #9cc42a;
    --sky-blue: #33a6d7;
    --stone-grey: #a3a3a3;
    --text-white: #ffffff;
  }
  * { margin: 0; padding: 0; box-sizing: border-box; }
  html, body {
    width: 1200px;
    height: 844px;
    overflow: hidden;
    background: var(--backdrop);
    font-family: "Montserrat", Arial, sans-serif;
  }
  .business-card {
    position: absolute;
    left: 183px;
    top: 167px;
    width: 834px;
    height: 509px;
    background: var(--card-white);
    overflow: hidden;
  }
  .brand-name {
    position: absolute;
    top: 70px;
    width: 100%;
    text-align: center;
    font-weight: 800;
    font-size: 35px;
    letter-spacing: 0.3px;
    color: var(--leaf-green);
    line-height: 1;
  }
  .owner-name {
    position: absolute;
    top: 112px;
    width: 100%;
    text-align: center;
    font-weight: 700;
    font-size: 20px;
    letter-spacing: 6px;
    color: var(--stone-grey);
    line-height: 1;
  }
  .brand-mark {
    position: absolute;
    top: 200px;
    left: 0;
    width: 100%;
    display: flex;
    justify-content: center;
    align-items: center;
    gap: 16px;
  }
  .brand-mark-dot {
    width: 44px;
    height: 44px;
    border-radius: 50%;
    background: var(--sky-blue);
  }
  .brand-mark-name {
    font-weight: 800;
    font-size: 44px;
    color: var(--sky-blue);
    line-height: 1;
  }
  .contact-band {
    position: absolute;
    left: 0;
    bottom: 0;
    width: 100%;
    height: 160px;
    background: var(--band-green);
    display: flex;
    flex-direction: column;
    justify-content: center;
    align-items: center;
    color: var(--text-white);
    font-weight: 600;
    font-size: 18px;
    line-height: 24px;
    text-align: center;
    padding-bottom: 10px;
  }
</style>
</head>
<body>
  <div class="business-card">
    <h1 class="brand-name">A WILLOW BREEZE</h1>
    <p class="owner-name">MARA QUINT</p>
    <div class="brand-mark">
      <span class="brand-mark-dot"></span>
      <span class="brand-mark-name">WB</span>
    </div>
    <div class="contact-band">
      <p class="contact-role">Massage Therapist and Flowing Pulse Method Practitioner</p>
      <p class="contact-address">2718 Bramblewood Lane, Lindenvale, AR 72000, 501-384-6190</p>
      <p class="contact-email">mara.willowbreeze@mailnest.example</p>
    </div>
  </div>
</body>
</html>
```